Award-winning book needs animated banner ad

I need an animated banner ad for my novel Halvorsen (see attached cover). Would like to show girl in grass, with slight waving of grass. To the right these words on dark background: A Midwestern girl adrift in a new town becomes engulfed in the struggles of two migrant brothers separated by an implacable border. Somewhere the title Halvorsen should appear in the font used on the book cover. Will run in Readers Chronicle. Specs are: Unit measurement Pixels (WxH): 728x90
Maximum Initial Download Fileweight: 150kb
Recommended Animation Length (seconds): 15
Acceptable file types: jpg, gif, or png

```html
<!DOCTYPE html>
<html lang="en">
<head>
<meta charset="utf-8">
<title>Halvorsen – Banner</title>
<link rel="stylesheet" href="https://fonts.googleapis.com/css2?family=Sacramento&family=Arimo:wght@400&display=swap">
<style>
  :root {
    --grass-gold: #b89a62;
    --grass-tan: #9c8556;
    --grass-olive: #6f6b4b;
    --dune-green: #3b4534;
    --sea-dark: #1f2a26;
    --sea-mist: #8c948d;
    --text-light: #ffffff;
    --page-bg: #ffffff;
  }
  html, body {
    margin: 0;
    padding: 0;
    width: 1200px;
    height: 149px;
    overflow: hidden;
    background: var(--page-bg);
  }
  .banner {
    position: relative;
    width: 1200px;
    height: 149px;
    overflow: hidden;
  }
  .banner__scene {
    position: absolute;
    inset: 0;
    width: 100%;
    height: 100%;
    display: block;
  }
  .banner__title {
    position: absolute;
    left: 255px;
    top: 16px;
    width: 360px;
    margin: 0;
    text-align: center;
    font-family: "Sacramento", cursive;
    font-weight: 400;
    font-size: 100px;
    line-height: 1.1;
    color: var(--text-light);
    text-shadow: 0 1px 4px rgba(0, 0, 0, 0.3);
  }
  .banner__tagline {
    position: absolute;
    left: 620px;
    top: 29px;
    width: 570px;
    margin: 0;
    font-family: "Arimo", Arial, sans-serif;
    font-size: 23.5px;
    line-height: 30px;
    text-align: center;
    color: var(--text-light);
  }
</style>
</head>
<body>
  <div class="banner">
    <svg class="banner__scene" viewBox="0 0 1200 149" preserveAspectRatio="none" role="img" aria-label="Photograph of a girl with a backpack sitting in tall dune grass, looking out over a dark sea">
      <defs>
        <linearGradient id="scene-land" x1="0" y1="0" x2="1" y2="0">
          <stop offset="0" stop-color="var(--grass-gold)"/>
          <stop offset="0.22" stop-color="var(--grass-tan)"/>
          <stop offset="0.45" stop-color="var(--grass-olive)"/>
          <stop offset="0.65" stop-color="var(--dune-green)"/>
          <stop offset="1" stop-color="var(--sea-dark)"/>
        </linearGradient>
        <linearGradient id="scene-sea" x1="0" y1="0" x2="0" y2="1">
          <stop offset="0" stop-color="var(--sea-dark)" stop-opacity="0.85"/>
          <stop offset="0.35" stop-color="var(--sea-dark)" stop-opacity="0.35"/>
          <stop offset="0.6" stop-color="var(--sea-dark)" stop-opacity="0"/>
        </linearGradient>
        <linearGradient id="scene-mist" x1="0" y1="0" x2="1" y2="0">
          <stop offset="0" stop-color="var(--sea-mist)" stop-opacity="0.55"/>
          <stop offset="0.35" stop-color="var(--sea-mist)" stop-opacity="0.15"/>
          <stop offset="0.6" stop-color="var(--sea-mist)" stop-opacity="0"/>
        </linearGradient>
        <linearGradient id="scene-grass-glow" x1="0" y1="0" x2="0" y2="1">
          <stop offset="0.5" stop-color="var(--grass-gold)" stop-opacity="0"/>
          <stop offset="1" stop-color="var(--grass-gold)" stop-opacity="0.35"/>
        </linearGradient>
      </defs>
      <rect width="1200" height="149" fill="url(#scene-land)"/>
      <rect x="300" width="900" height="149" fill="url(#scene-sea)"/>
      <rect width="1200" height="26" fill="url(#scene-mist)"/>
      <rect width="700" height="149" fill="url(#scene-grass-glow)"/>
    </svg>

    <h1 class="banner__title">Halvorsen</h1>

    <p class="banner__tagline">A Midwestern girl adrift in a new town becomes<br>engulfed in the struggles of two migrant brothers<br>separated by an implacable border.</p>
  </div>
</body>
</html>
```